New Business Card Design For Re-Branded Company (New Logo)

We recently switched our DBA and had a new logo designed. We now need new business cards made around our new logo. We would like to stick with the color scheme in our logo: White, Orange, and Blue. We want to see original bold designs that reflect our position in the solar energy sector but we prefer simple over complicated.

We are curious about vertical designs so if you can translate your design onto a vertical layout we would be open to look at it. We especially like a few designs we have seen on here that are vertical with a black or very dark gray background. They have our logo on one side and then the normal vertical business card on the other side.

I have included a screenshot of one of the samples we like, labeled sample.jpg and a file we were given as an example of our logo on a dark background.

At the same time we are satisfied to stay with what we have always had in a horizontal format. If it's not a lot of extra work for you, designs that are submitted in both horizontal and vertical formats will be greatly appreciated.

Please submit your original, bold, clean designs for consideration. Contact us with any questions or comments that may arise.

Thank you and Good Luck,

RT

```html
<!DOCTYPE html>
<html lang="en">
<head>
<meta charset="utf-8">
<title>Sunvale Power – Vertical Business Card</title>
<link href="https://fonts.googleapis.com/css2?family=Montserrat:wght@400;600;700&display=swap" rel="stylesheet">
<style>
  :root {
    --orange: #f08a24;
    --blue: #1f86d1;
    --card-black: #1b1b1c;
    --text-grey: #8a8a8a;
    --text-light: #e6e6e6;
    --backdrop: #d9d6d2;
  }
  * { box-sizing: border-box; margin: 0; padding: 0; }
  html, body {
    width: 1200px; height: 724px; overflow: hidden;
    background: var(--backdrop);
    font-family: "Montserrat", Arial, sans-serif;
  }
  .canvas {
    width: 1200px; height: 724px;
    display: flex; align-items: center; justify-content: center; gap: 44px;
  }
  .card {
    position: relative;
    width: 343px; height: 600px;
    background: var(--card-black);
    box-shadow: 0 10px 28px rgba(0,0,0,.28);
    overflow: hidden;
  }

  /* Back: contact side */
  .contact-side { padding: 54px 0 0 0; text-align: center; }
  .brand-mark {
    display: flex; flex-direction: column; align-items: center; gap: 18px;
  }
  .brand-dot {
    width: 96px; height: 96px; border-radius: 50%;
    background: var(--orange);
  }
  .brand-name {
    color: var(--orange); font-weight: 700; font-size: 26px; letter-spacing: .5px;
  }
  .person { margin-top: 44px; }
  .person-name { color: var(--orange); font-weight: 700; font-size: 20px; }
  .person-title { color: var(--text-grey); font-size: 13px; margin-top: 6px; }
  .person-mobile {
    color: var(--text-light); font-size: 13px; margin-top: 8px;
    display: flex; justify-content: center; align-items: center; gap: 7px;
  }
  .details {
    list-style: none; margin: 46px 0 0 58px; text-align: left;
  }
  .details li {
    display: flex; align-items: center; gap: 16px;
    color: var(--text-light); font-size: 12.5px; line-height: 1.4;
    margin-bottom: 16px;
  }
  .details .icon { width: 26px; height: 26px; flex: none; }
  .details b { font-weight: 700; }

  /* Front: brand side */
  .brand-side .backdrop-fill {
    position: absolute; inset: 0;
    background: linear-gradient(150deg,
      var(--orange) 0%, var(--card-black) 32%,
      var(--card-black) 68%, var(--blue) 100%);
  }
  .brand-side .brand-mark {
    position: absolute; top: 190px; left: 0; right: 0; gap: 26px;
  }
  .brand-side .brand-dot { width: 150px; height: 150px; }
</style>
</head>
<body>
<main class="canvas">

  <section class="card contact-side" aria-label="Card back with contact details">
    <div class="brand-mark">
      <span class="brand-dot"></span>
      <span class="brand-name">SUNVALE POWER</span>
    </div>

    <div class="person">
      <p class="person-name">Name Here</p>
      <p class="person-title">Title / Position</p>
      <p class="person-mobile">
        <svg width="10" height="14" viewBox="0 0 10 14"><rect x="1" y="1" width="8" height="12" rx="1.5" fill="none" stroke="#e6e6e6" stroke-width="1.4"/><line x1="4" y1="11" x2="6" y2="11" stroke="#e6e6e6" stroke-width="1.2"/></svg>
        123-456-0000
      </p>
    </div>

    <ul class="details">
      <li>
        <svg class="icon" viewBox="0 0 26 26"><path d="M3 13 L13 4 L23 13 M6 11 V22 H20 V11 M11 22 V16 H15 V22" fill="none" stroke="var(--orange)" stroke-width="1.8" stroke-linejoin="round"/></svg>
        <span>Unit Street<br>City, State Zip Code</span>
      </li>
      <li>
        <svg class="icon" viewBox="0 0 26 26"><path d="M7 3 L11 8 L9 11 C10 14 12 16 15 17 L18 15 L23 19 L20 23 C12 22 4 14 3 6 Z" fill="none" stroke="var(--orange)" stroke-width="1.8" stroke-linejoin="round"/></svg>
        <span><b>P</b>: 877-000-0001<br><b>F</b>: 877-000-0002</span>
      </li>
      <li>
        <svg class="icon" viewBox="0 0 26 26"><rect x="2" y="6" width="22" height="15" fill="none" stroke="var(--orange)" stroke-width="1.8"/><path d="M2 6 L13 15 L24 6" fill="none" stroke="var(--orange)" stroke-width="1.8"/></svg>
        <span>name@email.com</span>
      </li>
      <li>
        <svg class="icon" viewBox="0 0 26 26"><circle cx="13" cy="13" r="10" fill="none" stroke="var(--orange)" stroke-width="1.8"/><ellipse cx="13" cy="13" rx="4.5" ry="10" fill="none" stroke="var(--orange)" stroke-width="1.5"/><line x1="3" y1="13" x2="23" y2="13" stroke="var(--orange)" stroke-width="1.5"/><line x1="5" y1="8" x2="21" y2="8" stroke="var(--orange)" stroke-width="1.2"/><line x1="5" y1="18" x2="21" y2="18" stroke="var(--orange)" stroke-width="1.2"/></svg>
        <span>www.domain.com</span>
      </li>
    </ul>
  </section>

  <section class="card brand-side" aria-label="Card front with company name">
    <div class="backdrop-fill" role="img" aria-label="Decorative geometric background in orange, blue and dark grey"></div>
    <div class="brand-mark">
      <span class="brand-dot"></span>
      <span class="brand-name">SUNVALE POWER</span>
    </div>
  </section>

</main>
</body>
</html>
```